Einladungskarten-Design für Schützenverein
super gute Zusammenarbeit. Werde für weitere Arbeiten gerne darauf zurückkommen.
Zielgruppe
Wir sind ein Schützenverein und möchten mit einem neuzeitlichen Design für unser traditionelles Grümpelschiessen Werbung machen und die jüngere Generation für diesen schönen Sport begeistern.

```html
<!DOCTYPE html>
<html lang="de">
<head>
<meta charset="utf-8">
<title>Einladung zum Grümpelschiessen 2021</title>
<link rel="stylesheet" href="https://fonts.googleapis.com/css2?family=Montserrat:wght@800&family=Lato:wght@400;700;900&display=swap">
<style>
  :root {
    --navy: #2d3484;
    --navy-soft: #4a529c;
    --navy-deep: #1f2566;
    --yellow: #f2c500;
    --white: #ffffff;
    --photo-warm: #7a5a48;
    --photo-light: #d8d6d2;
  }
  * { margin: 0; padding: 0; box-sizing: border-box; }
  html, body { width: 1200px; height: 800px; overflow: hidden; background: #e9e9e9; }
  .card {
    position: relative; width: 1200px; height: 800px; overflow: hidden;
    background: var(--navy);
    font-family: "Lato", sans-serif; color: var(--white);
  }
  .backdrop {
    position: absolute; inset: 0;
    background: radial-gradient(ellipse at 62% 55%, var(--navy-soft) 0%, var(--navy) 55%, var(--navy-deep) 100%);
    opacity: .9;
  }
  .club-mark {
    position: absolute; left: 52px; top: 36px; width: 200px; height: 150px;
    background: var(--white); border: 6px solid var(--white);
    display: flex; flex-direction: column; align-items: center; justify-content: center; gap: 10px;
    outline: 3px solid var(--navy-deep);
  }
  .club-mark .square { width: 26px; height: 26px; background: var(--yellow); }
  .club-mark .name {
    font-family: "Lato", sans-serif; font-weight: 900; color: var(--navy);
    font-size: 17px; text-align: center; line-height: 1.2; text-transform: uppercase;
  }
  .headline {
    position: absolute; left: 330px; top: 60px;
    font-family: "Montserrat", sans-serif; font-weight: 800; line-height: 1.05;
    text-transform: uppercase;
  }
  .headline .lead { color: var(--white); font-size: 52px; display: block; }
  .headline .event { color: var(--yellow); font-size: 62px; }
  .headline .year { color: var(--white); font-size: 62px; }
  .date {
    position: absolute; left: 60px; top: 215px; width: 260px; text-align: center;
    font-size: 26px; line-height: 1.25;
  }
  .date .day { color: var(--yellow); font-weight: 700; display: block; }
  .photo {
    position: absolute; left: 0; top: 360px; width: 560px; height: 440px;
    background: linear-gradient(160deg, var(--photo-warm) 0%, #3b3231 45%, var(--photo-light) 100%);
  }
  .details {
    position: absolute; left: 575px; top: 255px; width: 590px;
    display: grid; grid-template-columns: 120px 1fr; row-gap: 18px; column-gap: 10px;
    font-size: 24px; line-height: 1.25;
  }
  .details dt { color: var(--yellow); font-weight: 700; }
  .details dd { color: var(--white); }
  .quote-mark {
    position: absolute; font-family: "Montserrat", sans-serif; font-weight: 800;
    font-size: 90px; line-height: 1; color: var(--white);
  }
  .quote-mark.open { left: 575px; top: 540px; }
  .quote-mark.close { left: 1120px; top: 660px; }
  .welcome {
    position: absolute; left: 640px; top: 585px; width: 520px;
    color: var(--yellow); font-weight: 700; font-size: 24px; line-height: 1.3;
  }
  .web-band {
    position: absolute; left: 560px; right: 0; bottom: 0; height: 92px;
    background: var(--yellow);
    display: flex; align-items: center; justify-content: center;
  }
  .web-band .url {
    font-family: "Lato", sans-serif; font-weight: 900; font-size: 46px; color: var(--navy);
  }
</style>
</head>
<body>
  <main class="card">
    <div class="backdrop" role="img" aria-label="Gedämpftes Foto einer Schiessanlage in blauer Tönung"></div>

    <div class="club-mark">
      <span class="square"></span>
      <span class="name">Schützenverein<br>Talberg</span>
    </div>

    <h1 class="headline">
      <span class="lead">Einladung zum</span>
      <span class="event">Grümpelschiessen</span> <span class="year">2021</span>
    </h1>

    <p class="date">
      <span class="day">Sonntag 29. August</span>
      08.00 - 12.00<br>Uhr durchgehend
    </p>

    <div class="photo" role="img" aria-label="Foto einer jungen Schützin mit Gewehr und Zielfernrohr, von hinten gesehen"></div>

    <dl class="details">
      <dt>Wo :</dt>
      <dd>BEIM SCHÜTZENHAUS TALBERG<br>(Parkplätze bei der Talstation der Sonnhaldebahn)</dd>
      <dt>Wer :</dt>
      <dd>Einzel, Paare und Familien &gt; einfach jedermann ob jung ob alt aus nah und fern, Frau und Mann</dd>
      <dt>Unser Angebot :</dt>
      <dd>Grümpelstich und Festwirtschaft mit Mittags-menü in herrlicher Umgebung</dd>
    </dl>

    <span class="quote-mark open">“</span>
    <p class="welcome">Wir laden Sie herzlich zu einem gemütlichen Sonntag ein und freuen uns auf Ihren Besuch und Ihre Teilnahme.</p>
    <span class="quote-mark close">”</span>

    <footer class="web-band">
      <span class="url">www.svtalberg.ch</span>
    </footer>
  </main>
</body>
</html>
```